Accountability Project Graphics

I want to create 10 social media graphics (new Instagram size 4:5 (1080 x 1350 pixels) focusing on our Kelmora Accountability App, using any of the 3 pictures attached. Use the attached pics only, NO RANDOM STOCK PHOTOGRAPHY. For the color scheme, use the landing page colors/fonts (attached).
You can add any of the 3 photos attached but I mainly need BOLD text that includes these headlines and sub-headlines on them.
Please NOTE for all the headlines below, also add this sub-headline on each graphic:
Stay Consistent with MB in Your Pocket!
Here are the headlines:
• Stop Starting Over Every Monday
• You don't need more willpower. You need more support
• Built for women who are tired of doing this alone
• When Motivation Fades, MB Checks In
• The Support System You've Been Missing
• Support When Motivation Disappears
• What if MB Checked in Every Day?
• The Missing Piece Isn't Another Diet
• Eat the food you love. Stay accountable every day.
• One Bad Meal Doesn't Mean You Failed
women over 40 trying to lose weight

```html
<!DOCTYPE html>
<html lang="en">
<head>
<meta charset="utf-8">
<title>Kelmora Accountability App – Social Graphics</title>
<link rel="stylesheet" href="https://fonts.googleapis.com/css2?family=Antonio:wght@700&family=Archivo:wdth,wght@125,900&display=swap">
<style>
  :root {
    --board: #5f5f61;
    --plum: #2f1b3d;
    --magenta: #c2356c;
    --pink-light: #f6c6da;
    --blush: #f3e3e6;
    --cream: #f4ece4;
    --white: #ffffff;
    --denim: #3b4f78;
    --grey-photo: #6d6a6c;
  }
  * { box-sizing: border-box; margin: 0; padding: 0; }
  html, body { width: 1200px; height: 602px; overflow: hidden; background: var(--board); }
  .board { position: relative; width: 1200px; height: 602px; }
  .card { position: absolute; width: 225px; height: 281px; overflow: hidden; background: var(--white); }
  .photo { position: absolute; inset: 0; }
  .headline {
    position: absolute; left: 0; right: 0; text-align: center; white-space: nowrap;
    font-family: "Antonio", "Oswald", sans-serif; font-weight: 700;
    letter-spacing: -0.02em; color: var(--plum);
  }
  .headline .line { display: block; }
  .headline.caps { text-transform: uppercase; }
  .headline.light { color: var(--white); }
  .tagline {
    position: absolute; left: 0; right: 0; top: 248px; text-align: center; white-space: nowrap;
    font-family: "Archivo", sans-serif; font-stretch: 125%; font-weight: 900;
    font-size: 8px; line-height: 8px; letter-spacing: 0.08em; text-transform: uppercase;
    color: var(--white);
  }
  .tagline.plum { color: var(--plum); }
  .tagline.magenta { color: var(--magenta); }
  .tagline.pink { color: var(--pink-light); }

  .c1 { left: 13px;  top: 14px; }  .c2 { left: 251px; top: 14px; }
  .c3 { left: 487px; top: 14px; }  .c4 { left: 725px; top: 14px; }
  .c5 { left: 962px; top: 14px; }
  .c6 { left: 13px;  top: 307px; } .c7 { left: 251px; top: 307px; }
  .c8 { left: 487px; top: 307px; } .c9 { left: 725px; top: 307px; }
  .c10 { left: 962px; top: 307px; }

  .duo-magenta { background: linear-gradient(160deg, var(--cream) 0%, #b98aa0 45%, var(--magenta) 100%); }
  .solo-dark { background: linear-gradient(90deg, var(--blush) 0%, #8e4f70 45%, var(--magenta) 100%); }
  .solo-dark::after { content: ""; position: absolute; inset: 0; background: linear-gradient(180deg, rgba(47,27,61,0) 30%, rgba(30,16,38,0.92) 75%, #2a1832 100%); }
  .duo-top-white { background: linear-gradient(180deg, var(--white) 0%, var(--cream) 30%, #c9b6a4 45%, var(--denim) 75%, #d8d3d8 100%); }
  .duo-bottom-white { background: linear-gradient(180deg, var(--denim) 0%, #8d8ba4 35%, #efe7ef 55%, var(--white) 70%); }
  .solo-magenta-top { background: linear-gradient(180deg, var(--magenta) 0%, #8c3c63 28%, #4b3a45 60%, #1c171b 100%); }
  .duo-grey { background: linear-gradient(180deg, #f2f2f2 0%, #bdb9bb 25%, var(--grey-photo) 60%, #3c383b 100%); }
  .hug-white { background: linear-gradient(180deg, var(--white) 0%, var(--white) 30%, #b07bb4 55%, #e46ea6 75%, var(--white) 100%); }
  .duo-white-top { background: linear-gradient(180deg, var(--white) 0%, var(--white) 25%, #c7a486 45%, var(--denim) 75%, #41506e 100%); }
  .hug-grey { background: linear-gradient(180deg, var(--white) 0%, var(--white) 30%, #8e6a82 55%, #a8a3a6 75%, var(--white) 100%); }
</style>
</head>
<body>
<main class="board">

  <section class="card c1">
    <div class="photo duo-magenta" role="img" aria-label="Photo of two smiling women standing together, magenta tint"></div>
    <h2 class="headline" style="top:178px;font-size:32px;line-height:34px;"><span class="line">Stop Starting</span><span class="line">Over Every Monday</span></h2>
    <p class="tagline" style="top:255px;">Stay consistent with<br>MB in your pocket!</p>
  </section>

  <section class="card c2">
    <div class="photo solo-dark" role="img" aria-label="Photo of a smiling woman in a black top, hand on hip"></div>
    <h2 class="headline light" style="top:181px;font-size:26px;line-height:27px;"><span class="line">The Support System</span><span class="line">You've Been Missing</span></h2>
    <p class="tagline pink" style="top:245px;">Stay consistent with<br>MB in your pocket!</p>
  </section>

  <section class="card c3">
    <div class="photo duo-top-white" role="img" aria-label="Photo of two laughing women standing together"></div>
    <h2 class="headline" style="top:13px;font-size:29px;line-height:31px;"><span class="line">The Missing Piece</span><span class="line">Isn't Another Diet</span></h2>
    <p class="tagline">Stay consistent with<br>MB in your pocket!</p>
  </section>

  <section class="card c4">
    <div class="photo solo-dark" role="img" aria-label="Photo of a smiling woman in a black top, hand on hip"></div>
    <h2 class="headline caps light" style="top:170px;font-size:23px;line-height:24px;"><span class="line">Built for women who</span><span class="line">are tired of</span><span class="line">doing this alone</span></h2>
    <p class="tagline magenta">Stay consistent with<br>MB in your pocket!</p>
  </section>

  <section class="card c5">
    <div class="photo duo-bottom-white" role="img" aria-label="Photo of two laughing women embracing, fading to white"></div>
    <h2 class="headline caps" style="top:148px;font-size:25px;line-height:25px;"><span class="line">Eat the food</span><span class="line">you love.</span><span class="line">Stay accountable</span><span class="line">every day.</span></h2>
    <p class="tagline magenta" style="top:255px;">Stay consistent with<br>MB in your pocket!</p>
  </section>

  <section class="card c6">
    <div class="photo solo-magenta-top" role="img" aria-label="Photo of a smiling woman in a black top, hand on hip"></div>
    <h2 class="headline light" style="top:16px;font-size:22px;line-height:24px;"><span class="line">When Motivation Fades,</span><span class="line">MB Checks In</span></h2>
    <p class="tagline">Stay consistent with<br>MB in your pocket!</p>
  </section>

  <section class="card c7">
    <div class="photo duo-grey" role="img" aria-label="Black and white photo of two laughing women together"></div>
    <h2 class="headline light" style="top:114px;font-size:31px;line-height:31px;"><span class="line">Support</span><span class="line">When</span><span class="line">Motivation</span><span class="line">Disappears</span></h2>
    <p class="tagline">Stay consistent with<br>MB in your pocket!</p>
  </section>

  <section class="card c8">
    <div class="photo hug-white" role="img" aria-label="Photo of two women hugging and laughing"></div>
    <h2 class="headline" style="top:13px;font-size:27px;line-height:28px;"><span class="line">One Bad Meal Doesn't</span><span class="line">Mean You Failed</span></h2>
    <p class="tagline plum">Stay consistent with<br>MB in your pocket!</p>
  </section>

  <section class="card c9">
    <div class="photo duo-white-top" role="img" aria-label="Photo of two laughing women standing together"></div>
    <h2 class="headline" style="top:9px;font-size:29px;line-height:31px;"><span class="line">What if MB Checked</span><span class="line">in Every Day?</span></h2>
    <p class="tagline">Stay consistent with<br>MB in your pocket!</p>
  </section>

  <section class="card c10">
    <div class="photo hug-grey" role="img" aria-label="Photo of two women hugging, muted purple tint"></div>
    <h2 class="headline caps" style="top:8px;">
      <span class="line" style="font-size:31px;line-height:32px;">You don't need</span>
      <span class="line" style="font-size:20px;line-height:21px;">More willpower.</span>
      <span class="line" style="font-size:22px;line-height:23px;">You need more support</span>
    </h2>
    <p class="tagline plum">Stay consistent with<br>MB in your pocket!</p>
  </section>

</main>
</body>
</html>
```